Packaging Design Job - Baby Diaper Rash Cream and Wipes Packaging Concepts Needed

Hello, Our baby brand “Mavory” is launching 2 new products – a Diaper Rash Cream and Diaper Wipes – and would like some creative design concepts for our product packaging.Mavory is a pharmaceutical brand that specializes in baby products. We are a mid – premium priced brand with a focus on targeting mothers between the ages of 18 – 35 years. Our products are positioned for mass market with other competitive brands such as Balmora, Pelvaxo, Quorel, and Lumiva, to give you a better understanding of the category. What we are looking for in our packaging is an ethical, pharmaceutical look that will appeal to mothers as a product that is safe and effective for their baby. The packaging should be clean, fresh, and consumer friendly, while still maintaining that this is a clinical product. The design concepts are a box design for the Diaper Rash Cream and a plastic packaging design for the Diaper Wipes. Attached you will find the Mavory logo and examples of Diaper Rash Cream box packaging and Diaper Wipes plastic packaging from competitors (to give you an idea of what shape of packaging we like). Please feel free to contact me should you have any questions.Thank you for your time and effort,Roska

Target Market(s)

We are a mid – premium priced brand with a focus on targeting mothers between the ages of 18 – 35 years.

Industry/Entity Type

Baby Care

Requirements
Must have
• Packaging design concepts for a box design for the Diaper Rash Cream and a plastic packaging design for the Diaper Wipes.
Nice to have
• Diaper Rash Cream box: 8 cm width, 8 cm length, 8 cm depth
• Diaper Wipes package: 23 cm width, 10.5 cm length, 4.5 cm depth

```html
<!DOCTYPE html>
<html lang="en">
<head>
<meta charset="utf-8">
<title>Mavory Baby Diaper Wipes Pack</title>
<link href="https://fonts.googleapis.com/css2?family=Yanone+Kaffeesatz:wght@400;500&family=Dancing+Script:wght@500&family=Roboto:wght@500;700&display=swap" rel="stylesheet">
<style>
  :root {
    --backdrop: #3b3b3b;
    --navy: #0f3f96;
    --navy-deep: #123779;
    --sky: #2aa6df;
    --film: #eceef1;
    --film-shade: #dfe2e7;
    --ink: #1b1b1b;
    --ink-navy: #1c3a7a;
    --white: #ffffff;
  }
  * { margin: 0; padding: 0; box-sizing: border-box; }
  html, body { width: 1200px; height: 834px; overflow: hidden; }
  body { background: var(--backdrop); position: relative; font-family: "Roboto", Arial, sans-serif; }

  .wipes-pack {
    position: absolute;
    left: 230px; top: 190px;
    width: 740px; height: 510px;
    background: linear-gradient(180deg, var(--film) 0%, var(--film-shade) 100%);
    overflow: hidden;
  }
  .seal { position: absolute; top: 0; bottom: 0; width: 26px;
    background: repeating-linear-gradient(180deg, rgba(0,0,0,.06) 0 3px, rgba(255,255,255,.0) 3px 7px); }
  .seal--left { left: 0; }
  .seal--right { right: 0; }

  .cloud-band { position: absolute; left: 0; top: 0; width: 740px; height: 200px; }

  .brand {
    position: absolute; left: 68px; top: 228px;
    display: flex; align-items: center; gap: 10px;
  }
  .brand__dot { width: 16px; height: 16px; border-radius: 50%; background: var(--navy); }
  .brand__name { font-family: "Roboto", Arial, sans-serif; font-weight: 700; font-size: 40px; color: var(--navy); letter-spacing: 2px; }

  .product-title {
    position: absolute; left: 312px; top: 212px;
    font-family: "Yanone Kaffeesatz", "Arial Narrow", sans-serif; font-weight: 400;
    font-size: 58px; color: var(--ink-navy); letter-spacing: .5px;
  }
  .protection {
    position: absolute; left: 425px; top: 286px;
    font-family: "Yanone Kaffeesatz", "Arial Narrow", sans-serif; font-weight: 400;
    font-size: 34px; color: var(--ink);
  }
  .weight-range { position: absolute; left: 443px; top: 345px; display: flex; align-items: flex-end; gap: 8px; }
  .weight-range__badge { background: var(--sky); border-radius: 6px; padding: 2px 12px; font-weight: 700; font-size: 28px; color: var(--navy-deep); }
  .weight-range__unit { font-weight: 700; font-size: 22px; color: var(--ink); padding-bottom: 3px; }

  .features { position: absolute; left: 72px; top: 314px; list-style: none; }
  .features__item { display: flex; align-items: center; gap: 14px; height: 35px;
    font-family: "Dancing Script", cursive; font-size: 23px; color: var(--ink); }
  .features__icon { width: 26px; height: 26px; flex: none; }

  .count { position: absolute; left: 460px; top: 446px; font-weight: 500; font-size: 27px; color: var(--navy-deep); }
</style>
</head>
<body>
  <main class="wipes-pack">
    <svg class="cloud-band" viewBox="0 0 740 200" aria-hidden="true">
      <path fill="var(--sky)" d="M0,0 H740 V118 Q700,88 670,103 Q640,78 610,98 Q580,83 550,103 Q520,98 500,118 Q470,108 450,133 Q420,128 400,158 Q350,158 330,178 Q280,203 220,188 Q170,203 130,173 Q90,158 70,138 Q40,113 0,118 Z"/>
      <path fill="var(--navy)" d="M0,0 H740 V110 Q700,80 670,95 Q640,70 610,90 Q580,75 550,95 Q520,90 500,110 Q470,100 450,125 Q420,120 400,150 Q350,150 330,170 Q280,195 220,180 Q170,195 130,165 Q90,150 70,130 Q40,105 0,110 Z"/>
    </svg>
    <div class="seal seal--left"></div>
    <div class="seal seal--right"></div>

    <div class="brand"><span class="brand__dot"></span><span class="brand__name">MAVORY</span></div>

    <h1 class="product-title">Baby Diaper Wipes</h1>
    <p class="protection">12 Hours Protection</p>
    <div class="weight-range"><span class="weight-range__badge">12 - 24</span><span class="weight-range__unit">lbs</span></div>

    <ul class="features">
      <li class="features__item">
        <svg class="features__icon" viewBox="0 0 26 26"><circle cx="13" cy="13" r="12" fill="var(--navy)"/><path d="M7 13h7M9 9l5 4-5 4M16 10q3 3 0 6" stroke="#fff" stroke-width="1.5" fill="none"/></svg>
        Fragrance free</li>
      <li class="features__item">
        <svg class="features__icon" viewBox="0 0 26 26"><circle cx="13" cy="13" r="12" fill="var(--navy)"/><path d="M7 9h12l-2 8H9z" stroke="#fff" stroke-width="1.5" fill="none"/></svg>
        Most Absorbent Diaper</li>
      <li class="features__item">
        <svg class="features__icon" viewBox="0 0 26 26"><circle cx="13" cy="13" r="12" fill="var(--navy)"/><circle cx="11" cy="15" r="4" fill="#fff"/><circle cx="17" cy="9" r="2" fill="#fff"/></svg>
        0% Chlorine Bleach</li>
      <li class="features__item">
        <svg class="features__icon" viewBox="0 0 26 26"><circle cx="13" cy="13" r="12" fill="var(--navy)"/><circle cx="13" cy="13" r="7" stroke="#fff" stroke-width="1.5" fill="none"/><path d="M13 9v4l3 2" stroke="#fff" stroke-width="1.5" fill="none"/></svg>
        Upto 12 hours Protection</li>
      <li class="features__item">
        <svg class="features__icon" viewBox="0 0 26 26"><circle cx="13" cy="13" r="12" fill="var(--navy)"/><path d="M13 6q5 7 0 13q-5-6 0-13z" fill="#fff"/></svg>
        Clinically Proven Hypoallergenic</li>
    </ul>

    <p class="count">20 pieces</p>
  </main>
</body>
</html>
```